professional looking data specialist website

I've recently had a new logo designed and I'm now looking to get a professional looking website built. This is for a new company that specialises in data. We look to support companies with business intelligence, report modelling, data governance to new european legislation (GDPR). We are offer consultancy or we can attend site and complete work when required. Our target arket is united kingdom wide and we are specifically aiming at small to medium sized companies.

Target Market(s)

small to medium enterprise companies from all industries

Industry/Entity Type

Professional Service

Coding

Coded - Design and coding required

Number of Pages Required

4 page

Font styles to use
Sans Serif

Colors

Designer to choose colors to be used in the design.

Requirements
Must have
• Professional look including the company logo, need to have ability to request more information from us so needs a inquiries page, seperate pages for the different offerings, data governance, report modelling, business intelligence implementation, data protection
Nice to have
• any website interaction, animation, etc
Should not have
• too many colours, too busy pages, must look professional

```html
<!DOCTYPE html>
<html lang="en">
<head>
<meta charset="utf-8">
<title>Corvane Data Ltd</title>
<link href="https://fonts.googleapis.com/css2?family=Open+Sans:wght@400;600;700&display=swap" rel="stylesheet">
<style>
:root{
  --blue:#0f66b7;
  --blue-dark:#0a57a0;
  --blue-light:#3f86d6;
  --grey:#8e9095;
  --grey-text:#6b6d72;
  --ink:#333;
  --footer:#e9e9e9;
  --bar:#d6d6d6;
  --white:#fff;
}
*{box-sizing:border-box;margin:0;padding:0}
html,body{width:694px;height:1200px;overflow:hidden;background:var(--white)}
body{font-family:"Open Sans",Arial,sans-serif;color:var(--ink);position:relative}
.abs{position:absolute}
.brand{font-size:12px;font-weight:600;color:var(--blue);display:flex;align-items:center;gap:6px}
.brand-mark{width:14px;height:14px;background:var(--blue)}
.call-tab{left:484px;top:0;width:150px;height:20px;background:var(--blue);color:var(--white);font-size:7.5px;display:flex;align-items:center;justify-content:center;gap:5px;clip-path:polygon(0 0,100% 0,92% 100%,8% 100%)}
.search{left:493px;top:32px;width:128px;height:21px;border:1px solid #ddd;background:#f4f4f4;font-size:7px;color:#999;padding:0 8px;display:flex;align-items:center;justify-content:space-between}
.nav{left:0;top:66px;width:694px;height:32px;background:var(--blue);display:flex;padding-left:57px}
.nav a{color:var(--white);font-size:9px;text-decoration:none;padding:0 8px;display:flex;align-items:center}
.nav a.active{background:#9a9a9a;padding:0 13px}
.hero{left:0;top:98px;width:694px;height:282px;background:linear-gradient(180deg,#6d6a7a 0%,#8a7f86 45%,#5a5566 70%,#403e4f 100%)}
.hero-title{top:208px;width:694px;text-align:center;color:var(--white);font-size:15px;font-weight:700}
.hero-sub{top:233px;width:694px;text-align:center;color:#eee;font-size:7px}
.btn-more{left:317px;top:257px;width:60px;height:20px;background:var(--blue);color:var(--white);font-size:7px;font-weight:700;display:flex;align-items:center;justify-content:center}
.welcome{top:399px;width:694px;text-align:center;font-size:8px;letter-spacing:1.5px;color:#444}
.welcome::before,.welcome::after{content:"";display:inline-block;width:38px;height:1px;background:#ccc;vertical-align:middle;margin:0 8px}
.about-title{top:414px;width:694px;text-align:center;font-size:19px;font-weight:700;letter-spacing:4px;color:var(--grey-text)}
.about-text{left:92px;top:446px;width:510px;text-align:center;font-size:7.5px;line-height:12px;color:#444}
.service{top:509px;width:140px;text-align:center}
.service .disc{width:112px;height:112px;border-radius:50%;margin:0 auto;display:flex;align-items:center;justify-content:center}
.disc.blue{background:var(--blue)}
.disc.grey{background:var(--grey)}
.service h3{margin-top:14px;font-size:10px;font-weight:600;color:var(--blue-light)}
.service p{margin-top:5px;font-size:6.8px;line-height:11.5px;color:#444}
.testimonials{left:0;top:729px;width:694px;height:272px;background:linear-gradient(135deg,#1a70c2,#0d5aa8 60%,#1466b6)}
.t-title{top:757px;width:694px;text-align:center;color:var(--white);font-size:15px;font-weight:700;letter-spacing:4px}
.quote{top:803px;width:170px;text-align:center;color:var(--white)}
.avatar{width:62px;height:62px;border-radius:50%;margin:0 auto;background:radial-gradient(circle at 50% 40%,#c9a58e,#6a5448);border:3px solid #e9e9e9}
.quote p{margin-top:14px;font-size:6.2px;font-weight:700;line-height:12px}
.quote h4{margin-top:9px;font-size:9px;font-weight:700}
.dots{top:971px;width:694px;display:flex;justify-content:center;gap:11px}
.dots span{width:4px;height:4px;border-radius:50%;background:var(--white)}
.footer{left:0;top:1001px;width:694px;height:168px;background:var(--footer)}
.f-head{font-size:10px;font-weight:700;letter-spacing:2.5px;color:var(--blue)}
.f-item{font-size:7px;color:#333;display:flex;gap:7px;align-items:flex-start;line-height:11px}
.f-item svg{flex:none;margin-top:1px}
.social{left:82px;top:1108px;display:flex;gap:6px}
.social span{width:15px;height:15px;background:var(--blue-light)}
.social span:nth-child(3){background:#c45a3c}
.social span:nth-child(4){background:#6b5a4a}
.input{left:347px;top:1082px;width:124px;height:18px;background:var(--white);border:1px solid #ddd;font-size:7px;color:#888;padding:0 8px;display:flex;align-items:center}
.subscribe{left:347px;top:1105px;width:64px;height:17px;background:var(--grey);color:var(--white);font-size:7px;font-weight:700;display:flex;align-items:center;justify-content:center}
.links{left:506px;top:1054px;list-style:none}
.links li{font-size:7px;line-height:15px;color:#333}
.links li::before{content:"»";margin-right:9px}
.bottom-bar{left:0;top:1169px;width:694px;height:31px;background:var(--bar);font-size:6.5px;color:#333;display:flex;align-items:center;justify-content:center}
</style>
</head>
<body>
<header>
  <div class="abs brand" style="left:57px;top:24px"><span class="brand-mark"></span>Corvane Data Ltd</div>
  <div class="abs call-tab">
    <svg width="7" height="7" viewBox="0 0 10 10"><path d="M2 1l2 2-1 1.5c.8 1.5 1.5 2.2 3 3L7.5 6l2 2-1.5 1.5C4.5 9 1 5.5.5 2.5z" fill="#fff"/></svg>
    Call Us: 1-800 555 0142
  </div>
  <div class="abs search">Search
    <svg width="8" height="8" viewBox="0 0 10 10"><circle cx="4" cy="4" r="3" fill="none" stroke="#777" stroke-width="1.5"/><path d="M6.3 6.3L9 9" stroke="#777" stroke-width="1.5"/></svg>
  </div>
  <nav class="abs nav">
    <a class="active">Home</a><a>About Us</a><a>Data Governance</a><a>Report Modelling</a><a>Business Intelligence</a><a>Data Protection</a><a>Inquiries</a><a>Contact Us</a>
  </nav>
</header>

<section>
  <div class="abs hero" role="img" aria-label="City skyline at dusk with a bridge over the river"></div>
  <svg class="abs" style="left:100px;top:203px" width="16" height="30" viewBox="0 0 16 30"><path d="M15 1L1 15l14 14" fill="none" stroke="#fff" stroke-width="1"/></svg>
  <svg class="abs" style="left:580px;top:203px" width="16" height="30" viewBox="0 0 16 30"><path d="M1 1l14 14L1 29" fill="none" stroke="#fff" stroke-width="1"/></svg>
  <h1 class="abs hero-title">Finibus Bonorum et Malorum</h1>
  <p class="abs hero-sub">Et harum quidem rerum facilis est et expedita distinctio.</p>
  <div class="abs btn-more">LEARN MORE</div>
</section>

<section>
  <div class="abs welcome">WELCOME</div>
  <h2 class="abs about-title">ABOUT US</h2>
  <p class="abs about-text">Lorem ipsum dolor sit amet, consectetur adipiscing elit, sed do eiusmod tempor incididunt ut labore et dolore magna aliqua. Ut enim ad minim veniam, quis nostrud exercitation ullamco laboris nisi ut aliquip ex ea commodo consequat. Duis aute irure dolor in reprehenderit in voluptate velit esse cillum dolore eu fugiat nulla pariatur.</p>

  <div class="abs service" style="left:68px">
    <div class="disc blue"><svg width="48" height="44" viewBox="0 0 48 44" fill="none" stroke="#fff" stroke-width="1.6"><path d="M4 12L24 2l20 10z"/><path d="M6 12h36v4H6z"/><path d="M11 16v18M18 16v18M24 16v18M30 16v18M37 16v18"/><path d="M5 34h38v4H5zM2 38h44v4H2z"/></svg></div>
    <h3>Data Governance</h3>
    <p>Sed ut perspiciatis unde omnis iste natus error sit voluptatem accusantium doloremque laudantium, totam...</p>
  </div>
  <div class="abs service" style="left:207px">
    <div class="disc grey"><svg width="44" height="40" viewBox="0 0 44 40" fill="none" stroke="#fff" stroke-width="1.8"><path d="M4 36h38"/><path d="M6 36V28h6v8M16 36V22h6v14M26 36V24h6v12M36 36V14h6v22"/><path d="M4 24l12-12 8 6 14-14"/><path d="M32 4h6v6"/></svg></div>
    <h3>Report Modelling</h3>
    <p>Sed ut perspiciatis unde omnis iste natus error sit voluptatem accusantium doloremque laudantium, totam...</p>
  </div>
  <div class="abs service" style="left:346px">
    <div class="disc blue"><svg width="46" height="46" viewBox="0 0 46 46" fill="none" stroke="#fff" stroke-width="1.6"><circle cx="17" cy="17" r="6"/><circle cx="17" cy="17" r="2"/><path d="M17 5v4M17 25v4M5 17h4M25 17h4M8.5 8.5l3 3M22.5 22.5l3 3M8.5 25.5l3-3M22.5 11.5l3-3"/><path d="M26 4c9 0 15 6 15 14l4 7h-4v6h-6v9M24 32v8"/></svg></div>
    <h3>Business Intelligence</h3>
    <p>Sed ut perspiciatis unde omnis iste natus error sit voluptatem accusantium doloremque laudantium, totam...</p>
  </div>
  <div class="abs service" style="left:486px">
    <div class="disc grey"><svg width="44" height="46" viewBox="0 0 44 46" fill="none" stroke="#fff" stroke-width="1.6"><path d="M4 2h18l6 6v14M4 2v36h18M22 2v6h6"/><text x="7" y="18" font-size="8" fill="#fff" stroke="none" font-family="Open Sans, sans-serif">101</text><text x="7" y="28" font-size="8" fill="#fff" stroke="none" font-family="Open Sans, sans-serif">01</text><rect x="24" y="28" width="16" height="14" rx="2"/><path d="M27 28v-5a5 5 0 0 1 10 0"/><text x="29.5" y="39" font-size="7" fill="#fff" stroke="none" font-family="Open Sans, sans-serif">0</text></svg></div>
    <h3>Data Protection</h3>
    <p>Sed ut perspiciatis unde omnis iste natus error sit voluptatem accusantium doloremque laudantium, totam...</p>
  </div>
</section>

<section>
  <div class="abs testimonials"></div>
  <h2 class="abs t-title">TESTIMONIALS</h2>
  <div class="abs quote" style="left:94px">
    <div class="avatar" role="img" aria-label="Portrait of client Marcus Hale"></div>
    <p>Sed ut perspiciatis unde omnis iste natus error sit voluptatem accusantium doloremque laudantium, totam rem aperiam, eaque...</p>
    <h4>-Marcus Hale</h4>
  </div>
  <div class="abs quote" style="left:262px">
    <div class="avatar" role="img" aria-label="Portrait of client Lena Ortiz"></div>
    <p>Sed ut perspiciatis unde omnis iste natus error sit voluptatem accusantium doloremque laudantium, totam rem aperiam, eaque...</p>
    <h4>- Lena Ortiz</h4>
  </div>
  <div class="abs quote" style="left:431px">
    <div class="avatar" role="img" aria-label="Portrait of client Ravi Kapoor"></div>
    <p>Sed ut perspiciatis unde omnis iste natus error sit voluptatem accusantium doloremque laudantium, totam rem aperiam, eaque...</p>
    <h4>- Ravi Kapoor</h4>
  </div>
  <div class="abs dots"><span></span><span></span><span></span><span></span></div>
</section>

<footer>
  <div class="abs footer"></div>
  <div class="abs brand" style="left:82px;top:1052px"><span class="brand-mark"></span>Corvane Data Ltd</div>
  <div class="abs f-head" style="left:82px;top:1087px">FOLLOW US</div>
  <div class="abs social"><span></span><span></span><span></span><span></span></div>

  <div class="abs f-head" style="left:207px;top:1029px">CONTACT US</div>
  <div class="abs f-item" style="left:207px;top:1053px"><svg width="7" height="7" viewBox="0 0 10 10"><path d="M2 1l2 2-1 1.5c.8 1.5 1.5 2.2 3 3L7.5 6l2 2-1.5 1.5C4.5 9 1 5.5.5 2.5z" fill="#0f66b7"/></svg>1-800 555 0199 (Phone)</div>
  <div class="abs f-item" style="left:207px;top:1077px"><svg width="7" height="7" viewBox="0 0 10 10"><rect x="0" y="3" width="10" height="7" fill="#0f66b7"/><rect x="2" y="0" width="6" height="4" fill="#0f66b7"/></svg>718-555-0173 (Fax)</div>
  <div class="abs f-item" style="left:207px;top:1101px"><svg width="7" height="7" viewBox="0 0 10 10"><path d="M0 4l5-4 5 4v6H0z" fill="#0f66b7"/></svg>hello@corvanedata.example</div>
  <div class="abs f-item" style="left:207px;top:1125px"><svg width="6" height="8" viewBox="0 0 8 10"><path d="M4 0a4 4 0 0 1 4 4c0 3-4 6-4 6S0 7 0 4a4 4 0 0 1 4-4z" fill="#0f66b7"/></svg>P O BOX 41207 MERTON<br>NY 10981</div>

  <div class="abs f-head" style="left:347px;top:1029px">NEWSLETTER</div>
  <p class="abs" style="left:347px;top:1052px;width:130px;font-size:7px;line-height:11.5px">Register Your email address to get information about us</p>
  <div class="abs input">Enter Email Id</div>
  <div class="abs subscribe">SUBSCRIBE</div>

  <div class="abs f-head" style="left:506px;top:1029px">QUICK LINKS</div>
  <ul class="abs links"><li>Home</li><li>About Us</li><li>Services</li><li>Contact Us</li></ul>

  <div class="abs bottom-bar">Copyrights © 2017, www.corvanedata.example</div>
</footer>
</body>
</html>
```